Pellora Digital - Layout Design

We need a web design for a new company based in Australia, called "Pellora Digital". We develop innovative custom web applications for Out Of Home, and Media companies.
Our initial website is a one page type of site. I've created a simple wireframe to show you what we need: https://plotgrid.cc/kq9Zt2
Here is a layout reference: http://brindlow.com/
( note - the designs needs to follow our branding guidelines (attached).
The top feature could be just solid color or an abstract subtle pattern or illustration that conveys the specialization of our business in the area of out of home, map, data.
In the attachment you will also find some images added for the work section.
Target Market(s)
Media and Advertising
Industry/Entity Type
Digital
Number of Pages Required
1 page
Look and feel

```html
<!DOCTYPE html>
<html lang="en">
<head>
<meta charset="utf-8">
<title>Pellora Digital</title>
<link rel="stylesheet" href="https://fonts.googleapis.com/css2?family=Open+Sans:wght@300;400;600;700&family=Lora:wght@400&display=swap">
<style>
:root{
  --green:#3fd26c;
  --green-dark:#2eb257;
  --cyan:#1cb3da;
  --cyan-head:#2ba7d6;
  --ink:#333;
  --muted:#555;
  --footer:#2e2e2e;
  --footer-line:#444;
  --white:#fff;
}
*{margin:0;padding:0;box-sizing:border-box}
html,body{width:1200px;height:4272px;overflow:hidden}
body{position:relative;background:var(--white);font-family:"Open Sans",Arial,sans-serif;color:var(--ink)}
.abs{position:absolute}
.site-header{left:0;top:0;width:1200px;height:132px;background:var(--green)}
.brand{left:228px;top:44px;font-size:34px;font-weight:700;color:#1d3b25}
.nav{right:228px;top:96px;display:flex;gap:30px;font-size:14px;color:var(--white)}
.nav a{color:var(--white);text-decoration:none}
.nav a.active{border-bottom:2px solid var(--white);padding-bottom:4px}
.hero-art{left:220px;top:150px;width:760px;height:370px;border-radius:48% 52% 40% 45%;background:radial-gradient(ellipse at 35% 45%,#f08a3c 0%,#e6465d 25%,#4fa7e0 55%,#e9eef2 80%,#fff 100%)}
.tagline{left:0;top:538px;width:1200px;text-align:center;font-family:"Lora",Georgia,serif;font-size:26px;color:#2c2c2c}
.hero-rule{left:228px;top:588px;width:744px;height:2px;background:#e4e4e4}
.band{left:0;width:1200px;background:var(--cyan);color:var(--white);text-align:center}
.band h2{font-weight:300;font-size:38px;padding-top:46px}
.band p{width:744px;margin:30px auto 0;font-size:14px;line-height:1.6}
.about{top:620px;height:252px}
.services{top:2232px;height:248px}
.section-title{left:0;width:1200px;text-align:center;font-weight:300;font-size:38px;color:var(--cyan-head)}
.intro{left:228px;width:744px;text-align:center;font-size:14px;font-weight:600;line-height:1.6}
.member-name{left:0;width:1200px;text-align:center;font-size:20px;color:#222}
.avatar{width:104px;height:104px;border-radius:50%;border:4px solid #cfe6f2;background:linear-gradient(160deg,#c9a48a,#8a5f4a 60%,#3b4a5a)}
.bio{left:252px;width:696px;font-size:14px;line-height:1.6;color:var(--muted)}
.advisors{left:0;top:1850px;width:1200px;text-align:center;font-size:20px}
.adv-name{width:300px;text-align:center;font-size:20px}
.adv-bio{width:290px;font-size:14px;line-height:1.6;color:var(--muted)}
.work-tile{left:228px;width:280px;height:200px}
.work-caption{left:228px;font-size:14px;color:var(--cyan-head)}
.work-text{left:640px;width:300px;font-size:14px;line-height:1.6;color:var(--muted)}
.work-text p+p{margin-top:22px}
.tile-label{display:flex;align-items:center;justify-content:center;font-size:40px;font-weight:600}
.site-footer{left:0;top:3980px;width:1200px;height:292px;background:var(--footer);color:#ddd;text-align:center;font-size:14px}
.site-footer h3{font-size:16px;font-weight:700;color:var(--white);padding-top:40px}
.site-footer p{margin-top:22px}
.legal{position:absolute;left:0;bottom:0;width:1200px;height:70px;border-top:1px solid var(--footer-line);line-height:70px;font-size:15px;color:var(--white)}
</style>
</head>
<body>
<header class="site-header abs">
  <div class="brand abs">Pellora Digital</div>
  <nav class="nav abs"><a class="active">Team</a><a>Services</a><a>Experience</a><a>Contact</a></nav>
</header>

<div class="hero-art abs" role="img" aria-label="Colourful illustration of media icons, screens and devices"></div>
<p class="tagline abs">We develop innovative custom web applications for Out Of Home, and Media companies</p>
<div class="hero-rule abs"></div>

<section class="band about abs">
  <h2>About Us</h2>
  <p>We are Pellora Digital, a team of innovators, thinkers and doers working collaboratively to produce great web apps. With decades of experience between us in media and out of home, we help businesses turn ideas into tools people enjoy using every day.</p>
</section>

<h2 class="section-title abs" style="top:888px">Key Team</h2>
<p class="intro abs" style="top:960px">Sed ut perspiciatis unde omnis iste natus error sit voluptatem accusantium doloremque laudantium, totam rem aperiam, eaque ipsa quae ab illo inventore veritatis et quasi architecto beatae vitae dicta sunt explicab</p>

<div class="member-name abs" style="top:1066px">Hanna Collery - CEO</div>
<div class="avatar abs" style="left:548px;top:1114px" role="img" aria-label="Portrait photo of Hanna Collery"></div>
<p class="bio abs" style="top:1236px">Sed ut perspiciatis unde omnis iste natus error sit voluptatem accusantium doloremque laudantium, totam rem aperiam, eaque ipsa quae ab illo inventore veritatis et quasi architecto beatae vitae dicta sunt explicabo.</p>

<div class="member-name abs" style="top:1324px">Dario Venn - CTO</div>
<div class="avatar abs" style="left:548px;top:1372px" role="img" aria-label="Portrait photo of Dario Venn"></div>
<p class="bio abs" style="top:1494px">Sed ut perspiciatis unde omnis iste natus error sit voluptatem accusantium doloremque laudantium, totam rem aperiam, eaque ipsa quae ab illo inventore veritatis et quasi architecto beatae vitae dicta sunt explicabo.</p>

<div class="member-name abs" style="top:1580px">Paul Ostrander - Executive Partner</div>
<div class="avatar abs" style="left:548px;top:1628px" role="img" aria-label="Portrait photo of Paul Ostrander"></div>
<p class="bio abs" style="top:1750px">Sed ut perspiciatis unde omnis iste natus error sit voluptatem accusantium doloremque laudantium, totam rem aperiam, eaque ipsa quae ab illo inventore veritatis et quasi architecto beatae vitae dicta sunt explicabo.</p>

<div class="advisors abs">Board of Advisors</div>
<div class="adv-name abs" style="left:230px;top:1904px">Mira Holt</div>
<div class="avatar abs" style="left:328px;top:1942px" role="img" aria-label="Portrait photo of Mira Holt"></div>
<p class="adv-bio abs" style="left:240px;top:2062px">Sed ut perspiciatis unde omnis iste natus error sit voluptatem accusantium doloremque laudantium, totam rem aperiam, eaque ipsa quae ab illo inventore veritatis et quasi architecto beatae vitae dicta sunt explicabo.</p>
<div class="adv-name abs" style="left:650px;top:1904px">Mira Holt</div>
<div class="avatar abs" style="left:748px;top:1942px" role="img" aria-label="Portrait photo of Mira Holt"></div>
<p class="adv-bio abs" style="left:660px;top:2062px">Sed ut perspiciatis unde omnis iste natus error sit voluptatem accusantium doloremque laudantium, totam rem aperiam, eaque ipsa quae ab illo inventore veritatis et quasi architecto beatae vitae dicta sunt explicabo.</p>

<section class="band services abs">
  <h2>Services</h2>
  <p>Sed ut perspiciatis unde omnis iste natus error sit voluptatem accusantium doloremque laudantium, totam rem aperiam, eaque ipsa quae ab illo inventore veritatis et quasi architecto beatae vitae dicta sunt explicabo.</p>
</section>

<h2 class="section-title abs" style="top:2520px">Experience</h2>

<div class="work-tile abs" style="top:2608px;background:linear-gradient(135deg,#7a3b8f,#2b5aa8 55%,#e9edf2)" role="img" aria-label="Varro Outdoor website showcase"></div>
<div class="work-caption abs" style="top:2818px">Varro Outdoor</div>
<div class="work-text abs" style="top:2620px"><p>A bold and progressive website for Australia and New Zealand that highlights Varro Outdoor's exciting new branding and extensive asset inventory.</p><p>Interactive and practical campaign planning tools have helped to position Varro as a forward thinking player in the OOH industry.</p></div>

<div class="work-tile abs tile-label" style="top:2852px;background:#25a9dd;color:var(--white)">Listwise</div>
<div class="work-caption abs" style="top:3062px">Listwise - Marketing Booking Platform</div>
<div class="work-text abs" style="top:2864px"><p>Listwise is a new generation Marketing Supply Chain management platform featuring various marketplace modules such as RFI/RFQ/RFP workflows, bidding, vendor portal, contract management.</p></div>

<div class="work-tile abs tile-label" style="top:3120px;background:#1fb0de;color:#1d2a33">Taskfold</div>
<div class="work-caption abs" style="top:3330px">Ocular Media</div>
<div class="work-text abs" style="top:3132px"><p>Sed ut perspiciatis unde omnis iste natus error sit voluptatem accusantium doloremque laudantium, totam rem aperiam, eaque ipsa quae ab illo inventore veritatis et quasi architecto beatae vitae dicta sunt explicabo.</p></div>

<div class="work-tile abs" style="top:3380px;background:linear-gradient(160deg,#3a3a3a,#1c1c1c 60%,#555)" role="img" aria-label="Quillo app shown on a laptop"></div>
<div class="work-caption abs" style="top:3590px">Quillo - Local Search Engine</div>
<div class="work-text abs" style="top:3392px"><p>Quillo is a location based social network where people ask questions, get answers and unlock rewards in real time by engaging with the community on the site.</p><p>The platform helps to connect locals with merchants rewarding them with exclusive offers and free products in exchange for social activities.</p></div>

<div class="work-tile abs" style="top:3644px;background:linear-gradient(135deg,#c96a3b,#e9c27a 40%,#7aa7c8 75%,#dfe6ea)" role="img" aria-label="Unmapped geography learning app screenshot"></div>
<div class="work-caption abs" style="top:3864px">Unmapped</div>
<div class="work-text abs" style="top:3656px"><p>Unmapped is a world first geography learning application created with the use of online maps.</p><p>Our team creates a learning experience personal to the user. As users study and memorise different countries they are awarded points and badges.</p></div>

<footer class="site-footer abs">
  <h3>CONTACT</h3>
  <p>Curious about what we can do to help your organization? Then please get in touch.</p>
  <p>info@pelloradigital.com.au</p>
  <p>02 9000 4417</p>
  <div class="legal">Pellora Digital Pty Ltd | Suite 4, Level 12 | Harbourline House | 8 Keel Street | Sydney NSW 2000 | Australia</div>
</footer>
</body>
</html>
```